Sports hypnotherapist needs electronic letterhead design

Need a simple but classy design for a letterhead that looks good when printed. Its for a hypnotherapist who specialises in elite sport. Should have my company name and address and website details on it. I specialise in footballers.
Should look good electronically and when printed.
Include all contact details as shown in the must haves.

Target Market(s)

Sports people, elite sport.

Industry/Entity Type

Hypnotherapy

Font styles to use
Sans Serif

Colors

Designer to choose colors to be used in the design.

Requirements
Must have
• NEEDS TO BE DESIGNED IN MS WORD
• Logo +
• Tidewell Path Hypnotherapists
• 27 Marlowby Close
• Bracknell
• RG14 3TX
• Tel: 07814 265173
• E: tidewellcoaching@brookmail.example
• www: http://www.tidewell-path.example.
• Colin Dearsley
• Clinical hypnotherapist, hypnoanalyst, mental resilience coach, MSc, Dip PHH
Nice to have
• A watermark?
• Plenty of space for the A4 letter
• Prints well.
Should not have
• Too much clutter.
• Too much colour that will be costly to print.

```html
<!DOCTYPE html>
<html lang="en">
<head>
<meta charset="utf-8">
<title>Tidewell Path Hypnotherapists – Letterhead</title>
<link href="https://fonts.googleapis.com/css2?family=Lato:wght@400;700&family=Tinos:wght@400;700&display=swap" rel="stylesheet">
<style>
  :root {
    --backdrop: #6b6b6b;
    --paper: #fafafa;
    --ink: #111111;
    --accent: #27bbe8;
    --letter-ink: #4a4a4a;
  }
  html, body { margin: 0; padding: 0; overflow: hidden; }
  body {
    width: 1200px; height: 1200px;
    background: var(--backdrop);
    position: relative;
  }
  .sheet {
    position: absolute;
    left: 219px; top: 30px;
    width: 653px; height: 978px;
    transform: scale(1.1656);
    transform-origin: top left;
    background: var(--paper);
    overflow: hidden;
    font-family: "Lato", sans-serif;
  }
  .sheet-shapes { position: absolute; inset: 0; }
  .brand-name {
    position: absolute; left: 45px; top: 80px;
    margin: 0;
    font: 700 31px/1.05 "Lato", sans-serif;
    color: var(--ink);
  }
  .practitioner {
    position: absolute; right: 48px; top: 81px;
    text-align: right; color: var(--ink);
  }
  .practitioner-name {
    margin: 0 0 13px; font-size: 11px; font-weight: 700; text-transform: uppercase;
  }
  .practitioner-name .first { color: var(--accent); font-weight: 400; }
  .practitioner-role { margin: 0; font-size: 11.5px; line-height: 15px; }
  .letter {
    position: absolute; left: 72px; top: 290px; width: 535px;
    font: 400 12.6px/15.7px "Tinos", serif;
    color: var(--letter-ink);
  }
  .letter p { margin: 0; }
  .letter .justified { text-align: justify; }
  .footer-address {
    position: absolute; left: 0; right: 0; top: 864px;
    text-align: center; font-size: 13.5px; line-height: 16px; color: var(--ink);
  }
  .footer-address p { margin: 0; }
  .footer-contact {
    position: absolute; left: 0; right: 0; top: 933px;
    text-align: center; font-size: 13.5px; line-height: 19px;
    color: #ffffff; letter-spacing: 0.06em;
  }
  .footer-contact p { margin: 0; }
  .footer-contact .label { color: var(--accent); font-weight: 700; }
</style>
</head>
<body>
  <div class="sheet">
    <svg class="sheet-shapes" viewBox="0 0 653 978" preserveAspectRatio="none" aria-hidden="true">
      <path d="M0,0 H330 Q120,18 0,80 Z" fill="var(--ink)"/>
      <path d="M240,10 Q420,-6 653,70 V0 H300 Q270,4 240,10 Z" fill="var(--accent)"/>
      <path d="M0,876 Q326,972 653,876 V978 H0 Z" fill="var(--ink)"/>
      <path d="M0,868 Q326,964 653,868" fill="none" stroke="var(--accent)" stroke-width="4"/>
    </svg>

    <h1 class="brand-name">Tidewell<br>Path</h1>

    <div class="practitioner">
      <p class="practitioner-name"><span class="first">Colin</span> Dearsley</p>
      <p class="practitioner-role">Clinical hypnotherapist, hypnoanalyst<br>mental resilience coach, MSc, Dip PHH</p>
    </div>

    <div class="letter">
      <p>Issuing date: May 5, 2012</p>
      <p style="margin-top:48px">Name of employee: Mr. xyz<br>Address of employee<br>address line 2</p>
      <p style="margin-top:48px"><strong>Ref: Promotion as an Assistant secretary</strong></p>
      <p style="margin-top:48px">Dear Mr. xyz,</p>
      <p class="justified" style="margin-top:16px">I have the pleasure to inform you that you have been promoted as assistant secretary in the share department of the company. You are required to take charge of the new assignment on 15<sup style="font-size:8px">th</sup> May, 2012. Please accept my hearty congratulations on your promotion.</p>
      <p class="justified" style="margin-top:16px">Your salary scale in the promoted cadre will be Tk. 16,000 and from 15th may, your basic salary will be fixed at Tk. 12,000 in the said scale. You will be entitled to all other allowances as applicable to the staff-II of the company. Other services conditions remain unchanged.</p>
      <p style="margin-top:16px">Please acknowledge receipt of this letter.</p>
      <p style="margin-top:48px">Yours sincerely,</p>
    </div>

    <div class="footer-address">
      <p>Tidewell Path Hypnotherapists</p>
      <p>27 Marlowby Close&nbsp; Bracknell, RG14 3TX</p>
    </div>

    <div class="footer-contact">
      <p><span class="label">Tel:</span> 07814 265173 <span class="label">Email:</span> tidewellcoaching@brookmail.example</p>
      <p>www: http://www.tidewell-path.example.</p>
    </div>
  </div>
</body>
</html>
```